Project Sign for Construction Company

Site contractor needs a 4'x8' sign to place on construction sites for advertising. Our company builds the infrastructure for new housing developments. These sign will be posted on the road side to be viewed by passing cars. I want a clean and bold look and feel that resembles my company logo.

Font styles to use
Other font styles liked:
• Hypatia Sans Pro

Colors

Designer to choose colors to be used in the design.

Requirements
Must have
• 555-318-2946 | Info@MarlowTerraworks.example
• CUC 8841907
• www.MarlowTerraworks.example
• Services
• Road Construction
• Site Preparation & Excavation
• Underground Utilities
• Shoreline Restoration
Nice to have
• Now Hiring
• Pipe Layers
• Foremen
• Equipment Operators
Should not have
• Should not have stock picture images used in the design, focus on logo and geometric shapes

```html
<!DOCTYPE html>
<html lang="en">
<head>
<meta charset="utf-8">
<title>Marlow Terraworks – Site Sign</title>
<link href="https://fonts.googleapis.com/css2?family=Exo+2:wght@500;600;800&family=Permanent+Marker&family=Roboto+Slab:wght@800&display=swap" rel="stylesheet">
<style>
  :root{
    --page:#e9ecef;
    --brand-blue:#2f55a4;
    --band-blue:#3453a3;
    --text-white:#ffffff;
    --sign-light:#ffffff;
    --sign-shade:#dfe2e6;
    --frame:#c9ccd0;
    --wood-dark:#5a3a1c;
    --wood-light:#8a6236;
    --chalk:#1c1c1e;
    --pin:#c9302c;
  }
  *{margin:0;padding:0;box-sizing:border-box}
  html,body{width:1200px;height:934px;overflow:hidden;background:var(--page)}
  .sign{
    position:absolute;left:30px;top:204px;width:1140px;height:526px;
    background:linear-gradient(180deg,var(--sign-light) 0%,#f3f4f6 55%,var(--sign-shade) 100%);
    border:10px solid var(--frame);
    overflow:hidden;
    font-family:"Exo 2",sans-serif;
  }
  .sign__swoosh{position:absolute;inset:0;width:100%;height:100%}
  .brand{position:absolute;left:36px;top:138px;display:flex;align-items:center;gap:16px}
  .brand__mark{width:32px;height:32px;background:var(--brand-blue);flex:none}
  .brand__name{font-weight:800;font-size:40px;letter-spacing:1.5px;color:var(--brand-blue);line-height:1;white-space:nowrap}
  .services{position:absolute;left:29px;top:268px;color:var(--brand-blue)}
  .services__title{font-weight:800;font-size:29px;letter-spacing:.5px;margin-bottom:10px;line-height:1.1}
  .services__list{list-style:none;display:grid;grid-template-columns:260px 330px;row-gap:4px;font-weight:500;font-size:20px;line-height:24px}
  .services__list li{position:relative;padding-left:22px;white-space:nowrap}
  .services__list li::before{content:"";position:absolute;left:2px;top:10px;width:6px;height:6px;background:var(--brand-blue)}
  .contact-band{
    position:absolute;left:0;right:0;bottom:0;height:108px;background:var(--band-blue);
    color:var(--text-white);text-align:center;font-weight:500;font-size:29px;line-height:38px;padding-top:16px;
  }
  .hiring{position:absolute;left:612px;top:18px;width:480px;height:380px}
  .hiring__string{position:absolute;left:0;top:0;width:480px;height:100px}
  .hiring__board{
    position:absolute;left:10px;top:78px;width:460px;height:282px;transform:rotate(-2deg);
    background:linear-gradient(135deg,var(--wood-light),var(--wood-dark));
    padding:14px;box-shadow:6px 8px 14px rgba(0,0,0,.35);
  }
  .hiring__chalk{
    width:100%;height:100%;background:var(--chalk);color:var(--text-white);
    text-align:center;padding-top:20px;overflow:hidden;
  }
  .hiring__now{font-family:"Permanent Marker","Impact",sans-serif;font-size:58px;line-height:1}
  .hiring__title{font-family:"Permanent Marker","Impact",sans-serif;font-size:86px;line-height:1}
  .hiring__roles{font-family:"Roboto Slab","Arial Black",sans-serif;font-weight:800;font-size:20px;line-height:25px;margin-top:10px;letter-spacing:.5px}
</style>
</head>
<body>
  <main class="sign" aria-label="Marlow Terraworks construction site sign">
    <svg class="sign__swoosh" viewBox="0 0 1120 506" preserveAspectRatio="none" aria-hidden="true">
      <path d="M150 40 Q600 -10 1120 120" fill="none" stroke="#cfd3d8" stroke-width="2"/>
      <path d="M230 120 Q650 70 1120 180" fill="none" stroke="#e1e4e8" stroke-width="3"/>
      <path d="M0 300 Q500 190 1120 260 L1120 506 L0 506 Z" fill="#ffffff" opacity=".55"/>
    </svg>

    <div class="brand">
      <span class="brand__mark"></span>
      <span class="brand__name">MARLOW TERRAWORKS</span>
    </div>

    <section class="services">
      <h2 class="services__title">SERVICES WE PROVIDED:</h2>
      <ul class="services__list">
        <li>Road Construction</li>
        <li>Site Preparation &amp; Excavation</li>
        <li>Underground Utilities</li>
        <li>Shoreline Restoration</li>
      </ul>
    </section>

    <aside class="hiring">
      <svg class="hiring__string" viewBox="0 0 480 100" aria-hidden="true">
        <path d="M160 92 L236 20 L318 88" fill="none" stroke="#222" stroke-width="3"/>
        <circle cx="236" cy="18" r="12" fill="var(--pin)"/>
        <circle cx="232" cy="14" r="4" fill="#e86a62"/>
      </svg>
      <div class="hiring__board">
        <div class="hiring__chalk">
          <div class="hiring__now">NOW</div>
          <div class="hiring__title">HIRING</div>
          <div class="hiring__roles">•PIPE LAYERS &nbsp;•FOREMEN<br>•EQUIPMENT OPERATORS</div>
        </div>
      </div>
    </aside>

    <footer class="contact-band">
      555-318-2946 | Info@MarlowTerraworks.example | CUC 8841907<br>
      www.MarlowTerraworks.example
    </footer>
  </main>
</body>
</html>
```